チラシは対象のお子様の親に見て頂きます。(1番)
地域の保健師・相談員(このようなサービスを紹介する人)や保育所等の先生にも見られると思います。
こちらで作ったものをアレンジして頂きたいと思います。
全て使用しなくでも大丈夫です。
写真を使用していきたいのですが、いま題材がないので、ネットのサンプル画像を利用して頂けると幸いです。どのような写真があればいいか教えて頂ければ、弊社での撮影も可能です。
A4
片面
• 高解像度JPG (.jpg)
• イラストレーター形式 (.ai)

```html
<!DOCTYPE html>
<html lang="ja">
<head>
<meta charset="utf-8">
<title>保育所等訪問支援 スタートします</title>
<link href="https://fonts.googleapis.com/css2?family=M+PLUS+Rounded+1c:wght@400;500;700;800&display=swap" rel="stylesheet">
<style>
  :root{
    --orange:#f0932b;
    --orange-dark:#e07a12;
    --orange-pale:#fff1df;
    --green:#7cbf3a;
    --green-pale:#eef7e2;
    --pink:#e8457a;
    --yellow:#f6c700;
    --blue:#3fa9e0;
    --purple:#a36ac7;
    --ink:#4a3a2a;
    --cream:#fffaf2;
    --white:#ffffff;
  }
  *{box-sizing:border-box;margin:0;padding:0}
  html,body{width:846px;height:1200px;overflow:hidden;background:var(--white)}
  body{font-family:"M PLUS Rounded 1c",sans-serif;color:var(--ink);position:relative}
  .flyer{position:relative;width:846px;height:1200px;overflow:hidden;background:var(--white)}

  .hero-photo{position:absolute;left:0;top:70px;width:846px;height:370px;
    background:linear-gradient(180deg,#f4f7fb 0%,#cfe0ec 35%,#b9c9a8 70%,#a9a58c 100%)}
  .title{position:absolute;left:24px;top:14px;display:flex;gap:6px}
  .title span{width:92px;height:92px;border-radius:50%;display:flex;align-items:center;justify-content:center;
    color:var(--white);font-size:60px;font-weight:800;line-height:1}
  .title span:nth-child(1){background:var(--pink)}
  .title span:nth-child(2){background:var(--orange)}
  .title span:nth-child(3){background:var(--yellow)}
  .title span:nth-child(4){background:var(--green)}
  .title span:nth-child(5){background:var(--blue)}
  .title span:nth-child(6){background:var(--purple)}
  .title span:nth-child(7){background:var(--pink)}
  .title span:nth-child(8){background:var(--orange)}
  .subtitle{position:absolute;right:30px;top:116px;font-size:36px;font-weight:800;color:var(--orange-dark);
    background:rgba(255,255,255,.85);padding:2px 14px;border-radius:24px}

  .concerns{position:absolute;left:0;top:440px;width:846px;height:132px;background:var(--orange);color:var(--white);
    padding:14px 40px 0}
  .concerns ul{list-style:none;display:grid;grid-template-columns:1fr 1fr;column-gap:30px;row-gap:4px;font-size:20px;font-weight:700}
  .concerns li::before{content:"✔ ";color:var(--yellow)}
  .concerns .lead{margin-top:10px;text-align:center;font-size:24px;font-weight:800;color:#fff6b0}

  .about{position:absolute;left:30px;top:586px;width:786px;display:flex;gap:16px;align-items:center}
  .about .label{flex:none;border:3px solid var(--orange);color:var(--orange-dark);font-weight:800;font-size:21px;
    padding:10px 14px;border-radius:10px;background:var(--cream)}
  .about p{font-size:15px;line-height:1.6;font-weight:500}

  .support{position:absolute;top:668px;width:384px;height:208px;border-radius:12px;padding:0 0 10px}
  .support.direct{left:30px;background:var(--green-pale)}
  .support.indirect{left:432px;background:var(--orange-pale)}
  .support h3{display:inline-block;color:var(--white);font-size:19px;font-weight:800;padding:5px 16px;border-radius:12px 0 12px 0}
  .direct h3{background:var(--green)}
  .indirect h3{background:var(--orange)}
  .support .catch{font-size:17px;font-weight:800;margin:8px 14px 6px}
  .direct .catch{color:#4f8f1b}
  .indirect .catch{color:var(--orange-dark)}
  .support ul{list-style:none;font-size:14px;line-height:1.55;margin:0 14px;width:220px}
  .support li::before{content:"■ ";font-size:11px}
  .direct li::before{color:var(--green)}
  .indirect li::before{color:var(--orange)}
  .support .art{position:absolute;right:12px;bottom:14px;width:130px;height:130px;border-radius:12px}
  .direct .art{background:linear-gradient(160deg,#fbe3cf,#d9ecc4)}
  .indirect .art{background:linear-gradient(160deg,#fde6d0,#f7cfa3)}

  .note{position:absolute;left:30px;top:884px;width:786px;font-size:12px;line-height:1.5}

  .flow{position:absolute;left:22px;top:916px;width:802px;height:122px;display:flex;align-items:center;gap:6px}
  .flow .badge{flex:none;width:96px;height:96px;border-radius:50%;background:var(--orange);color:var(--white);
    display:flex;align-items:center;justify-content:center;text-align:center;font-size:17px;font-weight:800;line-height:1.3}
  .flow .step{flex:1;height:118px;border:2px solid var(--orange);border-radius:10px;background:var(--cream);padding:6px 7px}
  .flow .step h4{font-size:13px;font-weight:800;color:var(--white);background:var(--orange);border-radius:6px;text-align:center;padding:2px 0;margin-bottom:5px}
  .flow .step p{font-size:11px;line-height:1.45}
  .flow .arrow{flex:none;width:12px;height:20px}

  .footer{position:absolute;left:0;top:1050px;width:846px;height:150px;background:var(--cream);border-top:4px solid var(--orange)}
  .brand{position:absolute;left:30px;top:52px;display:flex;align-items:center;gap:8px;font-size:18px;font-weight:700;color:var(--orange-dark)}
  .brand i{display:block;width:20px;height:20px;border-radius:50%;background:var(--green)}
  .contact{position:absolute;left:290px;top:18px;line-height:1.4}
  .contact .tel{display:flex;align-items:center;gap:8px;font-size:30px;font-weight:800;color:var(--orange-dark)}
  .contact .fax{font-size:22px;font-weight:700;margin-left:38px}
  .contact .info{font-size:13px;margin-top:4px}
  .map{position:absolute;right:24px;top:14px;width:200px;height:122px;border-radius:6px;
    background:linear-gradient(135deg,#eef0e6,#dfe6d3);border:1px solid #cfcab8}
</style>
</head>
<body>
<main class="flyer">
  <div class="hero-photo" role="img" aria-label="園庭で手をつないで走る笑顔の子どもたちの写真"></div>
  <h1 class="title"><span>保</span><span>育</span><span>所</span><span>等</span><span>訪</span><span>問</span><span>支</span><span>援</span></h1>
  <p class="subtitle">スタートします</p>

  <section class="concerns">
    <ul>
      <li>お友達となかなか遊べない</li>
      <li>行事への参加が難しい</li>
      <li>活動に集中できず、参加が難しい</li>
      <li>勉強が苦手でついていけない</li>
    </ul>
    <p class="lead">集団生活での心配事があるお子さんへ</p>
  </section>

  <section class="about">
    <h2 class="label">保育所等訪問支援</h2>
    <p>専門職のスタッフ（作業療法士、保育士、児童指導員など）が保育所などを訪問し、集団生活に溶け込めるよう、お子さまが過ごしやすくなるようサポートします。</p>
  </section>

  <section class="support direct">
    <h3>直接支援</h3>
    <p class="catch">お子さんと直接的に関わります</p>
    <ul>
      <li>お子さんが参加しやすいように手助けや学習を促します。</li>
      <li>発達支援を行う場面もあります。</li>
    </ul>
    <div class="art" role="img" aria-label="音楽に合わせて遊ぶ子どもたちのイラスト"></div>
  </section>

  <section class="support indirect">
    <h3>間接支援</h3>
    <p class="catch">所属先の担当の先生と一緒に考えていきます</p>
    <ul>
      <li>職員さんに対する環境作りの工夫を考えていきます。</li>
      <li>家庭でのサポートも一緒に考えます。</li>
    </ul>
    <div class="art" role="img" aria-label="先生と子どものイラスト"></div>
  </section>

  <p class="note">原則、月に1〜2回　対象：保育園、幼稚園、認定こども園、小学校、中学校、特別支援学校、放課後児童クラブ（学童保育）など集団生活を営む施設に通うお子さん</p>

  <section class="flow">
    <div class="badge">ご利用<br>の流れ</div>
    <div class="step"><h4>ご相談</h4><p>お電話でお気軽にご相談ください。ご家庭のご希望をお伺いします。</p></div>
    <svg class="arrow" viewBox="0 0 12 20"><path d="M0 0 L12 10 L0 20Z" fill="#f0932b"/></svg>
    <div class="step"><h4>所属先への連絡・同意</h4><p>保護者さまから所属先へご連絡いただき、訪問の同意を得ます。</p></div>
    <svg class="arrow" viewBox="0 0 12 20"><path d="M0 0 L12 10 L0 20Z" fill="#f0932b"/></svg>
    <div class="step"><h4>サービス申請・受給</h4><p>お住まいの市町村で申請し、受給者証を受け取ります。</p></div>
    <svg class="arrow" viewBox="0 0 12 20"><path d="M0 0 L12 10 L0 20Z" fill="#f0932b"/></svg>
    <div class="step"><h4>個別支援計画の作成</h4><p>面談を行い、お子さんに合わせた支援計画を作成します。</p></div>
    <svg class="arrow" viewBox="0 0 12 20"><path d="M0 0 L12 10 L0 20Z" fill="#f0932b"/></svg>
    <div class="badge">サービス<br>の開始</div>
  </section>

  <footer class="footer">
    <div class="brand"><i></i>こどもデイサービス ひだまり</div>
    <div class="contact">
      <p class="tel">
        <svg width="30" height="30" viewBox="0 0 24 24"><path d="M6.6 10.8a15 15 0 0 0 6.6 6.6l2.2-2.2a1 1 0 0 1 1-.25 11.4 11.4 0 0 0 3.6.57 1 1 0 0 1 1 1V20a1 1 0 0 1-1 1A17 17 0 0 1 3 4a1 1 0 0 1 1-1h3.5a1 1 0 0 1 1 1c0 1.25.2 2.45.57 3.57a1 1 0 0 1-.25 1z" fill="#e07a12"/></svg>
        TEL 0120-000-412
      </p>
      <p class="fax">FAX 0120-000-413</p>
      <p class="info">緑川市本町2丁目3-4<br>営業時間：8:30〜17:30　定休日：日・祝日</p>
    </div>
    <div class="map" role="img" aria-label="事業所周辺の案内地図"></div>
  </footer>
</main>
</body>
</html>
```